2 page brouchure for a Property Valuation company.

We require a 2 page brochure (printed front and back) for a property valuation company known as 'Brookmere Valuations'.

Brookmere valuations provides independent, reliable, accurate valuation services to our clients on the value of their properties to enable confidence and certainty in their decision.

The brochure is to be used to convey that the company provides valuation services for 8 main purposes and across 4 different property types.

The 8 main purposes for valuation include:
- Pre-Purchase Valuations
- Stamp Duty Valuations
-Capital Gains Tax (CGT)Valuations
-Unit Entitlement Valuations
-Family Law and Litigation Valuations
-Easement Valuations
-Wills & Probate Valuations
-Insolvency/Asset Realisation Valuations

The 4 main property types are:
-Residential
-Commercial
-Industrial
-Retail.

The brochure should have a title page, a page for the services, a page for the property types and a rear page with contact details.
Contact detail will include;
email:
phone :
Post :
website:

The words 'property valuation and advisory services' should be used at the front of the brochure.

The brochure should be professional and is used to convey information using visual aid and is to be used for promotion.

Our main colors are dark green and grey as seen in our logo.

We have attached our logo to add to the brochure and visit our website at: www.brookmerevaluations-example.com.au for more information about the company.

Please let me know if there are any further questions.

Target Market(s)

Solicitors/Lawyers
Accountants
Surveyors
Builders/Developers

Requirements
Must have
• Logo Colors, Logo, 8 Main services, 4 main property types, contact details.
Nice to have
• Should have concise visual aids to convey message.

Please add that we provide fast 48 hour turnaround for short form valuations. Maybe use a visual aid to convey this.

```html
<!DOCTYPE html>
<html lang="en">
<head>
<meta charset="utf-8">
<title>Brookmere Valuations – Property Valuation and Advisory Services</title>
<link href="https://fonts.googleapis.com/css2?family=Montserrat:wght@500;600;700&family=Oswald:wght@400;500;600&family=Roboto+Condensed:wght@600;700&display=swap" rel="stylesheet">
<style>
  :root {
    --green: #0f7a3e;
    --green-dark: #0b5e30;
    --charcoal: #3a3a3c;
    --charcoal-dark: #2b2b2d;
    --grey-light: #e9eaea;
    --white: #ffffff;
    --photo-grass: #6f9a45;
    --photo-sky: #c9d6d8;
    --photo-warm: #8a6a4a;
  }
  * { margin: 0; padding: 0; box-sizing: border-box; }
  html, body { width: 849px; height: 1200px; overflow: hidden; background: var(--white); }
  .page { position: relative; width: 849px; height: 1200px; overflow: hidden; background: var(--white); }

  .side-band { position: absolute; left: 0; top: 0; width: 290px; height: 520px; background: var(--charcoal); }
  .side-band-mark { position: absolute; left: 120px; top: 32px; width: 72px; height: 72px; border-radius: 14px; background: #4a4a4d; }

  .brand { position: absolute; left: 430px; top: 62px; display: flex; align-items: center; gap: 18px; }
  .brand-square { width: 76px; height: 76px; background: var(--green); }
  .brand-name { font-family: "Montserrat", sans-serif; font-weight: 600; font-size: 31px; line-height: 1.15; letter-spacing: 4px; color: var(--charcoal); text-transform: uppercase; }

  .hero-photo { position: absolute; left: 200px; top: 172px; width: 649px; height: 470px; border-top-left-radius: 110px; overflow: hidden;
    background: linear-gradient(180deg, var(--photo-sky) 0%, #aab9b2 38%, var(--photo-warm) 52%, var(--photo-grass) 70%, #4f7a2f 100%); }

  .hero-panel { position: absolute; left: 0; top: 222px; width: 340px; height: 420px; }
  .hero-title { position: absolute; left: 34px; top: 300px; width: 250px; color: var(--white); font-family: "Oswald", sans-serif; text-transform: uppercase; line-height: 1.05; }
  .hero-title .light { display: block; font-weight: 400; font-size: 40px; }
  .hero-title .bold { display: block; font-weight: 600; font-size: 52px; }

  .side-photo { position: absolute; left: 0; width: 240px; }
  .side-photo.statue { top: 652px; height: 170px; background: linear-gradient(135deg, #5a4a36 0%, #a88a5c 55%, #d8c7a2 100%); }
  .side-photo.coins { top: 832px; height: 213px; background: linear-gradient(160deg, #e6e2da 0%, #b7a88d 60%, #8c7450 100%); }
  .side-foot { position: absolute; left: 0; top: 1055px; width: 240px; height: 145px; background: var(--charcoal-dark); }

  .purposes { position: absolute; left: 262px; top: 664px; width: 575px; }
  .purposes-title { font-family: "Roboto Condensed", sans-serif; font-weight: 700; font-size: 30px; line-height: 36px; color: var(--green); text-transform: uppercase; letter-spacing: 0.3px; margin-bottom: 8px; white-space: nowrap; }
  .purpose-list { list-style: none; }
  .purpose { display: flex; align-items: center; gap: 14px; height: 40px; font-family: "Roboto Condensed", sans-serif; font-weight: 600; font-size: 24px; color: var(--charcoal); text-transform: uppercase; white-space: nowrap; }
  .purpose svg { flex: none; width: 30px; height: 30px; }

  .turnaround { position: absolute; left: 262px; top: 1045px; width: 587px; height: 155px; background: var(--charcoal); color: var(--white); text-align: center; font-family: "Oswald", sans-serif; text-transform: uppercase; padding-top: 8px; }
  .turnaround .lead { display: block; font-weight: 500; font-size: 40px; line-height: 1.05; }
  .turnaround .hours { display: block; font-weight: 600; font-size: 78px; line-height: 1.0; }
  .turnaround .tail { display: block; font-weight: 400; font-size: 19px; line-height: 1.2; letter-spacing: 0.5px; }
</style>
</head>
<body>
<div class="page">
  <div class="side-band"><div class="side-band-mark"></div></div>

  <div class="brand">
    <div class="brand-square"></div>
    <div class="brand-name">Brookmere<br>Valuations</div>
  </div>

  <div class="hero-photo" role="img" aria-label="Photo of a smiling family lying together on a lawn in front of a modern home"></div>

  <svg class="hero-panel" viewBox="0 0 340 420" aria-hidden="true">
    <path d="M0 0 H180 Q300 0 300 120 V420 H0 Z" fill="var(--green)"/>
  </svg>
  <h1 class="hero-title">
    <span class="light">Property</span>
    <span class="bold">Valuation</span>
    <span class="light">and</span>
    <span class="bold">Advisory</span>
    <span class="light">Services</span>
  </h1>

  <div class="side-photo statue" role="img" aria-label="Photo of a scales of justice statue beside law books"></div>
  <div class="side-photo coins" role="img" aria-label="Photo of a hand stacking coins"></div>
  <div class="side-foot"></div>

  <section class="purposes">
    <h2 class="purposes-title">The 8 main purposes for valuation</h2>
    <ul class="purpose-list">
      <li class="purpose"><svg viewBox="0 0 30 30"><circle cx="15" cy="15" r="15" fill="var(--green)"/><path d="M8 15 L15 9 L22 15 V22 H8 Z" fill="#fff"/></svg>Pre-purchase valuations</li>
      <li class="purpose"><svg viewBox="0 0 30 30"><circle cx="15" cy="15" r="15" fill="var(--green)"/><rect x="10" y="7" width="10" height="16" fill="#fff"/><rect x="12" y="11" width="6" height="2" fill="var(--green)"/><rect x="12" y="15" width="6" height="2" fill="var(--green)"/></svg>Stamp duty valuations</li>
      <li class="purpose"><svg viewBox="0 0 30 30"><circle cx="15" cy="15" r="15" fill="var(--green)"/><rect x="8" y="16" width="3" height="6" fill="#fff"/><rect x="13" y="12" width="3" height="10" fill="#fff"/><rect x="18" y="8" width="3" height="14" fill="#fff"/></svg>Capital gains tax (CGT)valuations</li>
      <li class="purpose"><svg viewBox="0 0 30 30"><circle cx="15" cy="15" r="15" fill="var(--green)"/><rect x="10" y="7" width="10" height="16" fill="#fff"/><rect x="12" y="9" width="2" height="2" fill="var(--green)"/><rect x="16" y="9" width="2" height="2" fill="var(--green)"/><rect x="12" y="13" width="2" height="2" fill="var(--green)"/><rect x="16" y="13" width="2" height="2" fill="var(--green)"/></svg>Unit entitlement valuations</li>
      <li class="purpose"><svg viewBox="0 0 30 30"><circle cx="15" cy="15" r="15" fill="var(--green)"/><path d="M15 7 V22 M9 10 H21 M9 10 L7 16 H11 Z M21 10 L19 16 H23 Z M11 22 H19" stroke="#fff" stroke-width="2" fill="#fff"/></svg>Family law and litigation valuations</li>
      <li class="purpose"><svg viewBox="0 0 30 30"><circle cx="15" cy="15" r="15" fill="var(--green)"/><path d="M7 21 L14 8 L16 8 L23 21 Z" fill="#fff"/><rect x="14" y="10" width="2" height="10" fill="var(--green)"/></svg>Easement valuations</li>
      <li class="purpose"><svg viewBox="0 0 30 30"><circle cx="15" cy="15" r="15" fill="var(--green)"/><path d="M9 8 H19 L21 10 V22 H9 Z" fill="#fff"/><path d="M12 18 L18 12" stroke="var(--green)" stroke-width="2"/></svg>Wills &amp; probate valuations</li>
      <li class="purpose"><svg viewBox="0 0 30 30"><circle cx="15" cy="15" r="15" fill="var(--green)"/><rect x="8" y="10" width="14" height="11" rx="1" fill="#fff"/><rect x="12" y="8" width="6" height="3" fill="#fff"/><rect x="8" y="14" width="14" height="2" fill="var(--green)"/></svg>Insolvency/asset realisation valuations</li>
    </ul>
  </section>

  <div class="turnaround">
    <span class="lead">We provide fast</span>
    <span class="hours">48 Hour</span>
    <span class="tail">Turnaround for short form valuations</span>
  </div>
</div>
</body>
</html>
```